Business card for Chicago based Private Equity Company

We need a business card for our PE company called Crestline Partners. We want a simple and clean, yet creative card design. The back side should reflect our logo. Also would like to see embossed ideas. Should reflect strength and growth. Our logo is attached. Also need editable file. Details are as follows for Business Card:

Dale Moravec Co-Founder 2750 Larkin Avenue Suite 410 Oak Brook, IL 60587 http://www.crestlinepartnersllc.example (D) 630.555.0142 (C) 312.555.0178 (E) dm@crestlinepartnersllc.example

```html
<!DOCTYPE html>
<html lang="en">
<head>
<meta charset="utf-8">
<title>Crestline Partners – Business Card</title>
<link href="https://fonts.googleapis.com/css2?family=Jura:wght@400;500;600&display=swap" rel="stylesheet">
<style>
  :root{
    --page:#e6e7e9;
    --card-top:#ffffff;
    --card-bottom:#eceded;
    --ink:#2b2b2d;
    --blue-light:#20a6e8;
    --blue-deep:#1a5fc2;
    --charcoal:#3a3a3c;
    --mark-blue:#1f86d8;
  }
  html,body{margin:0;padding:0;width:1200px;height:900px;overflow:hidden;background:var(--page);}
  .canvas{position:relative;width:1200px;height:900px;}
  .card{
    position:absolute;left:100px;top:165px;width:1000px;height:570px;
    border-radius:44px;overflow:hidden;
    background:linear-gradient(160deg,var(--card-top) 0%,var(--card-bottom) 100%);
    box-shadow:0 10px 30px rgba(0,0,0,.12);
    font-family:"Jura",sans-serif;color:var(--ink);
  }
  .brand{position:absolute;left:90px;top:140px;width:330px;text-align:center;}
  .brand-mark{width:110px;height:110px;border-radius:50%;border:13px solid var(--mark-blue);box-sizing:border-box;margin:0 auto 28px;}
  .brand-name{font-size:38px;font-weight:500;letter-spacing:3px;text-transform:uppercase;color:var(--ink);line-height:1.15;margin:0;}
  .divider{position:absolute;left:475px;top:80px;width:3px;height:320px;background:var(--ink);}
  .details{position:absolute;left:515px;top:80px;font-size:19px;line-height:1.3;}
  .person-name{font-weight:600;font-size:22px;letter-spacing:.5px;text-transform:uppercase;margin:0;}
  .person-role{margin:0 0 0 8px;font-size:19px;}
  .address{margin:40px 0 0 56px;font-size:19px;}
  .contact-list{list-style:none;margin:34px 0 0 80px;padding:0;font-size:17px;}
  .contact-list li{display:flex;align-items:center;gap:12px;height:27px;white-space:nowrap;}
  .contact-list svg{width:18px;height:18px;flex:none;}
  .band{position:absolute;left:0;bottom:0;width:1000px;height:150px;}
</style>
</head>
<body>
<div class="canvas">
  <div class="card">
    <div class="brand">
      <div class="brand-mark"></div>
      <p class="brand-name">Crestline Partners</p>
    </div>

    <div class="divider"></div>

    <div class="details">
      <p class="person-name">Dale Moravec</p>
      <p class="person-role">Co-Founder</p>
      <p class="address">2750 Larkin Avenue Suite 410<br>Oak Brook, IL 60587</p>
      <ul class="contact-list">
        <li><svg viewBox="0 0 24 24"><path fill="#2b2b2d" d="M6.6 10.8a15 15 0 0 0 6.6 6.6l2.2-2.2c.3-.3.7-.4 1-.2 1.1.4 2.3.6 3.6.6.6 0 1 .4 1 1V20c0 .6-.4 1-1 1A17 17 0 0 1 3 4c0-.6.4-1 1-1h3.5c.6 0 1 .4 1 1 0 1.3.2 2.5.6 3.6.1.3 0 .7-.2 1z"/></svg>630.555.0142</li>
        <li><svg viewBox="0 0 24 24"><rect x="6" y="2" width="12" height="20" rx="2" fill="none" stroke="#2b2b2d" stroke-width="2"/><circle cx="12" cy="18" r="1.3" fill="#2b2b2d"/></svg>312.555.0178</li>
        <li><svg viewBox="0 0 24 24"><rect x="3" y="8" width="18" height="12" rx="1" fill="#2b2b2d"/><rect x="7" y="3" width="10" height="6" fill="none" stroke="#2b2b2d" stroke-width="2"/></svg>630.555.0199</li>
        <li><svg viewBox="0 0 24 24"><rect x="2" y="5" width="20" height="14" rx="1" fill="#2b2b2d"/><path d="M2 6l10 7 10-7" fill="none" stroke="#fff" stroke-width="1.6"/></svg>dm@crestlinepartnersllc.example</li>
        <li><svg viewBox="0 0 24 24"><circle cx="12" cy="12" r="9" fill="none" stroke="#2b2b2d" stroke-width="2"/><ellipse cx="12" cy="12" rx="4" ry="9" fill="none" stroke="#2b2b2d" stroke-width="1.6"/><path d="M3 12h18M5 7h14M5 17h14" stroke="#2b2b2d" stroke-width="1.4"/></svg>www.crestlinepartnersllc.example</li>
      </ul>
    </div>

    <svg class="band" viewBox="0 0 1000 150" preserveAspectRatio="none">
      <defs>
        <linearGradient id="bandBlue" x1="0" y1="0" x2="1" y2="0">
          <stop offset="0" stop-color="#1a5fc2"/>
          <stop offset=".55" stop-color="#20a6e8"/>
          <stop offset="1" stop-color="#1a5fc2"/>
        </linearGradient>
      </defs>
      <path d="M0 88 C 320 72, 680 45, 1000 5 L1000 18 C 680 58, 320 86, 0 100 Z" fill="#3a3a3c"/>
      <path d="M0 96 C 320 82, 680 55, 1000 14 L1000 150 L0 150 Z" fill="url(#bandBlue)"/>
    </svg>
  </div>
</div>
</body>
</html>
```